Photo Booth and Chocolate Fountain Rental Flyer

I need a design that looks appealing and elegant for people who are having parties or weddings. It is a photo booth and chocolate fountain rental company. I would like it to look fun for the photo booth and delicious for the chocolate fountain. I would like some pictures to showcase the services and pricing options on it too. My logo needs to be put somewhere on the flyer also. You can check out my website for more information www.tvr-parties.com I want it to be a little different from the website and contain pictures of photo booth strips and chocolate fountains.

Industry/Entity Type

It Company

Requirements
Must have
• Must Have:
- our logo
our contact info
imagery of the photobooth experience
editable (change specials and marketing)
works in color
Nice to have
• A backside with the different packages of the photo booth and fountain

```html
<!DOCTYPE html>
<html lang="en">
<head>
<meta charset="utf-8">
<title>TVR Parties – Photo Booth &amp; Chocolate Fountain Flyer</title>
<link href="https://fonts.googleapis.com/css2?family=Didact+Gothic&family=Montserrat:wght@600;700&display=swap" rel="stylesheet">
<style>
  :root{
    --gold:#f3b21e;
    --gold-soft:#f5c94f;
    --amber:#f0a82a;
    --ink:#2a2523;
    --band:#2b2826;
    --cocoa:#3b2a20;
    --cocoa-deep:#22170f;
    --cream:#fff;
    --muted:#c9c0b4;
    --panel-text:#eee1d2;
    --silver:#8a8a8a;
    --platinum:#6e6862;
  }
  *{box-sizing:border-box;margin:0;padding:0}
  html,body{width:850px;height:1200px;overflow:hidden;background:#fff}
  body{font-family:"Didact Gothic",Arial,sans-serif;color:var(--ink)}
  .flyer{position:relative;width:850px;height:1200px;overflow:hidden;background:#fff}
  .abs{position:absolute}

  /* Front */
  .hero-photo{left:0;top:0;width:850px;height:370px;
    background:linear-gradient(100deg,#fbf6ee 0%,#f1e4d0 30%,#d9b894 52%,#b88a66 68%,#e9dccb 85%,#f6f0e8 100%)}
  .package{top:83px;width:112px;text-align:center}
  .package-tab{height:26px;line-height:26px;color:#fff;font-family:"Montserrat",sans-serif;font-weight:700;font-size:10.5px;white-space:nowrap;border-radius:6px 6px 0 0}
  .package-body{background:rgba(255,255,255,.95);height:78px;padding-top:8px;font-size:9px;line-height:1.25;border-radius:0 0 4px 4px}
  .package-price{font-family:"Montserrat",sans-serif;font-weight:700;font-size:17px;margin-top:3px}
  .package--silver{left:47px}.package--silver .package-tab{background:var(--silver)}
  .package--gold{left:162px}.package--gold .package-tab{background:var(--gold)}
  .package--gold .package-body{background:var(--gold-soft)}
  .package--platinum{left:285px}.package--platinum .package-tab{background:var(--platinum)}
  .includes{left:47px;top:197px;width:455px;height:136px;background:rgba(255,255,255,.93);border-radius:6px;text-align:center;font-size:9.6px;line-height:1.4;padding:10px 12px}
  .includes strong{font-family:"Montserrat",sans-serif;font-size:10px}
  .includes p+p{margin-top:7px}
  .contact{left:560px;top:318px;width:250px;text-align:center;font-family:"Montserrat",sans-serif;font-weight:700;color:var(--ink)}
  .contact-label{font-size:13px}
  .contact-phone{font-size:24px;letter-spacing:.5px}
  .stripe{left:0;top:370px;width:850px;height:22px;display:flex;gap:4px;background:#fff}
  .stripe span{flex:1;background:var(--gold)}
  .stripe span:first-child{flex:.7;background:#3a3633}
  .intro{left:0;top:392px;width:850px;height:200px;background:var(--band);color:var(--muted);font-size:8.3px;line-height:1.4;overflow:hidden}
  .intro-left{position:absolute;left:60px;top:30px;width:340px;text-align:center}
  .intro-left h2{font-size:9.2px;font-weight:normal;color:#e9e2d8;margin-bottom:7px}
  .intro-left p{margin-bottom:7px}
  .intro-right{position:absolute;left:440px;top:78px;width:370px;text-align:center}
  .intro-right p{margin-bottom:8px}
  .brand{position:absolute;left:520px;top:12px;width:220px;text-align:center;font-family:"Montserrat",sans-serif;font-weight:600;font-size:32px;color:var(--gold);letter-spacing:2px}

  /* Back */
  .menu{left:0;top:608px;width:850px;height:592px;background:radial-gradient(ellipse at 50% 35%,#4a3526 0%,var(--cocoa) 45%,var(--cocoa-deep) 100%)}
  .menu-tab{top:613px;height:40px;width:285px;background:#2a211b;border-radius:8px 8px 0 0;text-align:center;line-height:40px;font-family:"Montserrat",sans-serif;font-weight:700;font-size:19px;color:var(--amber)}
  .menu-tab--booth{left:107px}
  .menu-tab--fountain{left:483px}
  .menu-panel{top:653px;height:405px;background:rgba(110,80,60,.55);border-radius:4px;text-align:center;color:var(--panel-text);overflow:hidden}
  .menu-panel h3{font-family:"Montserrat",sans-serif;color:var(--amber);font-weight:600}
  .menu-panel--booth{left:58px;width:338px;font-size:8px;line-height:1.2;padding-top:16px}
  .menu-panel--booth h3{font-size:9px}
  .menu-panel--booth .tier{margin-bottom:10px}
  .menu-panel--fountain{left:458px;width:327px;font-size:7.2px;line-height:1.17;padding-top:12px}
  .menu-panel--fountain h3{font-size:8px}
  .menu-panel--fountain .tier{margin-bottom:7px}
  .booth-photo{left:58px;top:850px;width:338px;height:208px;background:linear-gradient(135deg,#7a5a44 0%,#b48a68 40%,#5c4232 70%,#8d6a50 100%)}
  .menu-foot{top:1073px;text-align:center;color:#f1e7dc;font-size:9.6px;line-height:1.35}
  .menu-foot h4{font-family:"Montserrat",sans-serif;font-size:11px;color:var(--amber);font-weight:700}
  .menu-foot--booth{left:58px;width:338px}
  .menu-foot--fountain{left:440px;width:365px}
</style>
</head>
<body>
<div class="flyer">

  <!-- Front -->
  <div class="abs hero-photo" role="img" aria-label="Close-up photograph of a smiling couple embracing"></div>

  <div class="abs package package--silver">
    <div class="package-tab">Silver Package</div>
    <div class="package-body">3 Hour Rental<br>+<br>CD<div class="package-price">$499.00</div>+Tax</div>
  </div>
  <div class="abs package package--gold">
    <div class="package-tab">Gold Package</div>
    <div class="package-body">4 Hour Rental<br>+<br>CD<div class="package-price">$699.00</div>+Tax</div>
  </div>
  <div class="abs package package--platinum">
    <div class="package-tab">Platinum Package</div>
    <div class="package-body">6 Hour Rental<br>+<br>CD, Scrap book<div class="package-price">$899.00</div>+Tax</div>
  </div>

  <div class="abs includes">
    <p><strong>All packages include:</strong><br>
    Unlimited prints | Double 2x6 prints | Choice of Color or B/W<br>
    Custom Graphic, Prop Box, and Photo Booth Decor | Free Web Hosting<br>
    Fantastic Host and Technician | Free Delivery-Setup-Tear Down</p>
    <p><strong>We also provide:</strong><br>
    Photo Strip Frames and Magnets | Disc of all images | Scrap Booking Service</p>
  </div>

  <div class="abs contact">
    <div class="contact-label">Contact Us On</div>
    <div class="contact-phone">805-555-0142</div>
  </div>

  <div class="abs stripe"><span></span><span></span><span></span><span></span></div>

  <section class="abs intro">
    <div class="intro-left">
      <h2>Why Choose TVR Parties?<br>Our Booth Holds up to 12 People!<br>One of the Largest Booths on the Central Coast</h2>
      <p>Top of the Line 18 mega pixel Lumora Digital SLR Camera,<br>22 inch Touch Screen Interface (Check out how cool looks)<br>Studio Professional Lighting (No Flashes or Red Eye)<br>Custom Decorated Booths that you have never seen before!</p>
      <p><strong>We accept Cash, Check, and Credit Card</strong></p>
      <p>* Deposit of $100 is required to save your date<br>* Don't see a package that fits for your event give us a call or e-mail and<br>We can create a custom package</p>
    </div>
    <div class="brand">TVR Parties</div>
    <div class="intro-right">
      <p>Make your events appealing and unforgettable with our specialties. We are a one of a kind event company, specializing in offering you fabulous fun in our photo booths, delicious chocolate fountains, and one of a kind decor. We can proudly say that our company exceptionally makes people's dreams a reality.</p>
      <p>We offer services to weddings, corporate events, bridal showers, baby showers, and birthday parties. Have your events decorated with style, elegance and custom design just for you by TVR Parties.</p>
      <p>So what are you waiting for? Let us make your event amazing with lots of amazing decor, delicious chocolate and excellent photos!</p>
    </div>
  </section>

  <!-- Back -->
  <div class="abs menu"></div>
  <div class="abs menu-tab menu-tab--booth">Photo Booth</div>
  <div class="abs menu-tab menu-tab--fountain">Chocolate Fountain</div>

  <div class="abs menu-panel menu-panel--booth">
    <div class="tier"><h3>Package 1</h3>$325.00+Tax<br>Feeds up to 100 Guests<br>Includes:<br>One 19" Chocolate Fountain | 3 Gourmet Dipping Items</div>
    <div class="tier"><h3>Package 2</h3>$425.00+Tax<br>Feeds up to 150 Guests<br>Includes:<br>Two 19" Chocolate Fountains | 4 Gourmet Dipping Items</div>
    <div class="tier"><h3>Package 3</h3>$525.00+Tax<br>Feeds up to 200 Guests<br>Includes:<br>Three 19" Chocolate Fountains | 5 Gourmet Dipping Items</div>
  </div>
  <div class="abs booth-photo" role="img" aria-label="Photo of guests posing with props inside the photo booth"></div>

  <div class="abs menu-panel menu-panel--fountain">
    <div class="tier"><h3>Package 1</h3>$325.00+Tax<br>Feeds up to 100 Guests<br>Includes:<br>One 19" Chocolate Fountain | 3 Hr Service<br>Your Choice of Premium Chocolate<br>Beautiful Display Including Skewers, Napkins, and Plates | 3 Gourmet Dipping Items</div>
    <div class="tier"><h3>Package 2</h3>$425.00+Tax<br>Feeds up to 150 Guests<br>Includes:<br>Two 19" Chocolate Fountains | 3 Hr Service<br>Two Choices of Premium Chocolate<br>Beautiful Display Including Skewers, Napkins, and Plates | 4 Gourmet Dipping Items</div>
    <div class="tier"><h3>Package 3</h3>$525.00+Tax<br>Feeds up to 200 Guests<br>Includes:<br>Three 19" Chocolate Fountains | 3 Hr Service<br>Your Choice of 3 Premium Chocolates<br>Beautiful Display Including Skewers, Napkins, and Plates | 5 Gourmet Dipping Items</div>
    <div class="tier"><h3>Kids Party Package</h3>$245.00+Tax<br>Feeds up to 50 guests<br>Includes:<br>2 Hrs Service | One 19" Chocolate Fountain<br>One Choice of Chocolate<br>Themed Display Including Skewers, Napkins, and Plates<br>3 Dipping Items</div>
    <div class="tier"><h3>Chocolate Flavors</h3>Premium Milk Chocolate, Dark Chocolate, White Chocolate, Mint<br>Chocolate, Marshmallow Cream, and Caramel<br>Extras:<br>Colored Premium Chocolate $85.00 | Fountain Add on $100.00 (up to<br>3 Fountains Only) | Additional Dipping Items 1.50 per guest<br>Additional Hour $45.00 | Additional Chocolate $50.00</div>
  </div>

  <div class="abs menu-foot menu-foot--booth">
    <h4>All packages include</h4>
    Beautiful Display | Skewers, Napkins, Plates | Dipping Items<br>
    Choice of Milk, Dark, and White Chocolate | 3 Hr Service<br>
    Fantastic Host | Delivery, set-up, and cleanup removal | Extras<br>
    Colored Chocolate $85.00 | Additional Dipping Items 1.50 per guest<br>
    Additional Hour $45.00
  </div>
  <div class="abs menu-foot menu-foot--fountain">
    <h4>Dipping Items</h4>
    Strawberries | Marshmallows | Churros | Pineapple | Bananas | Bacon<br>
    Pretzels | Creamos | Puffed Rice Treats | Goldies | Spicoff | Brownie Bites<br>
    Pound Cake Bites | Graham Crackers<br>
    Think of anything else? Let me know, I can get it!
  </div>

</div>
</body>
</html>
```